Mira Business card

This card is to represent me as a coach and Velumora facilitator
Double sided in colour
A beautiful, simple and elegant design that indicates movement and is modern, FRESH and uplifting. Please don’t use much black and use the attached Velumora logo.
Preferred colours - white, lighter blues and fresh greens

Target Market(s)
Business people - potential clients age 35 up
Industry/Entity Type
Business
Requirements
Must have
-  Text for the front :
Lumiwell Path
Mira Hollis
Biocentric Coach
Co-Director, Velumora Academy of Australia
E: mira@velumora.com.au
M: 0472 913 548.
W: velumora.com.au
Biocentric Coaching for Individuals, Teams and Organisations
Velumora for Children, Adults and Social development projects
Text for the back :
The Velumora system facilitates the expression of human potential for health, happiness and humanity through music, movement and group interaction. It was developed by Esteban Ruiz Pallares, a Chilean anthropologist and clinical psychologist, in 1976.
Creative use of the logo - integrating it within the design - e.g perhaps using it as the O in Velumora,
Please feature the heron from the logo or a another elegant graceful stylized heron.

```html
<!DOCTYPE html>
<html lang="en">
<head>
<meta charset="utf-8">
<title>Mira Hollis – Business Card</title>
<link href="https://fonts.googleapis.com/css2?family=Lato:wght@300;400;700&display=swap" rel="stylesheet">
<style>
  :root {
    --bg: #e8eaeb;
    --card-white: #f6f7f7;
    --brand-blue: #2f9fd8;
    --back-blue: #33a7dd;
    --heron-mid: #b9d8ee;
    --heron-pale: #dcebf6;
    --ink: #2b2f33;
    --white: #ffffff;
  }
  * { box-sizing: border-box; margin: 0; padding: 0; }
  html, body {
    width: 1200px; height: 900px; overflow: hidden;
    background: var(--bg);
    font-family: "Lato", Arial, sans-serif;
  }
  .canvas { position: relative; width: 1200px; height: 900px; }

  .card {
    position: absolute; top: 172px;
    width: 340px; height: 556px;
    box-shadow: 0 2px 10px rgba(0,0,0,.12);
    overflow: hidden;
  }

  /* Front */
  .card-front { left: 220px; background: var(--card-white); }
  .heron-area {
    position: absolute; left: 70px; top: 300px;
    width: 250px; height: 250px; border-radius: 50%;
    background: radial-gradient(circle at 50% 45%, var(--heron-mid) 0%, var(--heron-pale) 70%);
  }
  .heron-ring {
    position: absolute; left: 58px; top: 288px;
    width: 274px; height: 274px; border-radius: 50%;
    border: 2px dotted var(--heron-mid);
  }
  .wordmark {
    position: absolute; left: 30px; top: 32px;
    font-size: 38px; font-weight: 400; letter-spacing: 3px;
    color: var(--brand-blue);
  }
  .tagline {
    position: absolute; left: 32px; top: 80px;
    font-size: 12px; letter-spacing: 2px; text-transform: uppercase;
    color: var(--brand-blue);
  }
  .identity { position: absolute; right: 30px; top: 106px; text-align: right; }
  .name {
    font-size: 23px; font-weight: 400; letter-spacing: 1px;
    text-transform: uppercase; color: var(--brand-blue); margin-bottom: 4px;
  }
  .role { font-size: 15px; line-height: 1.3; color: var(--ink); }
  .divider { position: absolute; display: block; }
  .front-divider { left: 56px; top: 226px; }
  .contacts {
    position: absolute; left: 44px; top: 256px;
    display: grid; grid-template-columns: 22px auto; row-gap: 4px;
    font-size: 15px; color: var(--ink);
  }
  .contacts .label { color: var(--brand-blue); font-size: 17px; }
  .contacts .web { font-weight: 700; }
  .services {
    position: absolute; right: 26px; bottom: 40px; width: 250px;
    text-align: right; font-size: 14px; line-height: 1.35; color: var(--ink);
  }

  /* Back */
  .card-back { left: 640px; background: var(--back-blue); }
  .logo-panel {
    position: absolute; left: 18px; top: 18px; right: 18px; height: 250px;
    background: var(--card-white); border-radius: 14px;
    display: flex; align-items: center; justify-content: center; gap: 12px;
  }
  .logo-dot { width: 22px; height: 22px; border-radius: 50%; background: var(--brand-blue); }
  .logo-name { font-size: 30px; letter-spacing: 3px; color: var(--brand-blue); }
  .back-divider { left: 56px; top: 292px; }
  .about {
    position: absolute; left: 30px; right: 30px; top: 326px;
    text-align: center; color: var(--white);
    font-size: 15px; font-weight: 400; line-height: 1.5;
  }
</style>
</head>
<body>
<main class="canvas">

  <section class="card card-front" aria-label="Card front">
    <div class="heron-ring"></div>
    <div class="heron-area" role="img" aria-label="Stylised pale blue heron in flight, wings raised"></div>
    <div class="wordmark">VELUMORA</div>
    <div class="tagline">Lumiwell Path</div>
    <div class="identity">
      <h1 class="name">Mira Hollis</h1>
      <p class="role">Biocentric Coach<br>Co-Director, Velumora Academy<br>of Australia</p>
    </div>
    <svg class="divider front-divider" width="228" height="14" viewBox="0 0 228 14">
      <line x1="8" y1="7" x2="220" y2="7" stroke="var(--brand-blue)" stroke-width="1.6"/>
      <rect x="2" y="3" width="8" height="8" transform="rotate(45 6 7)" fill="var(--brand-blue)"/>
      <rect x="218" y="3" width="8" height="8" transform="rotate(45 222 7)" fill="var(--brand-blue)"/>
    </svg>
    <div class="contacts">
      <span class="label">M</span><span>0472 913 548</span>
      <span class="label">E</span><span>mira@velumora.com.au</span>
      <span class="label">W</span><span class="web">velumora.com.au</span>
    </div>
    <p class="services">Biocentric Coaching for Individuals, Teams and Organisations<br>Velumora for Children, Adults and Social development projects</p>
  </section>

  <section class="card card-back" aria-label="Card back">
    <div class="logo-panel">
      <span class="logo-dot"></span>
      <span class="logo-name">VELUMORA</span>
    </div>
    <svg class="divider back-divider" width="228" height="14" viewBox="0 0 228 14">
      <line x1="8" y1="7" x2="220" y2="7" stroke="var(--white)" stroke-width="1.6"/>
      <rect x="2" y="3" width="8" height="8" transform="rotate(45 6 7)" fill="var(--white)"/>
      <rect x="218" y="3" width="8" height="8" transform="rotate(45 222 7)" fill="var(--white)"/>
    </svg>
    <p class="about">The Velumora system facilitates the expression of human potential for health, happiness and humanity through music, movement and group interaction. It was developed by Esteban Ruiz Pallares, a Chilean anthropologist and clinical psychologist, in 1976.</p>
  </section>

</main>
</body>
</html>
```